vantoreq realty business card

We need a Business card for our new business. The logo was designed by BrushQuill, and the text We want on the back is:
REAL ESTATE INVESTMENTS
- BUY, RENOVATE, SELL AND RENT RESIDENTIAL PROPERTIES
- FULL HOME REHABBING , REMODELING AND INTERIOR DESIGN
- HOME STAGING SERVICES
- WHOLESALE INVESTOR PROPERTIES
- MAKE CASH OFFERS ON HOUSES IN ANY CONDITION AND IN ANY SITUATION
- PRIVATE MONEY INVESTOR PROGRAMS WITH 6-12% RETURNS
- PAY CASH REWARDS FOR REFFERALS
- CONCIERGE SERVICE

Business

```html
<!DOCTYPE html>
<html lang="en">
<head>
<meta charset="utf-8">
<title>Vantoreq Realty — Business Card</title>
<link href="https://fonts.googleapis.com/css2?family=Open+Sans:ital,wght@0,400;0,600;1,400;1,700&display=swap" rel="stylesheet">
<style>
  :root {
    --page: #eceae7;
    --card-white: #ffffff;
    --card-mist: #e4e5e6;
    --brand-blue: #6ec9dd;
    --brand-grey: #8a8b8d;
    --text-grey: #7b7c7e;
    --panel-grey: #909192;
    --ink-light: #ffffff;
    --shadow: rgba(0, 0, 0, 0.18);
  }
  * { box-sizing: border-box; margin: 0; padding: 0; }
  html, body { width: 1200px; height: 900px; overflow: hidden; }
  body {
    background: var(--page);
    font-family: "Open Sans", Arial, sans-serif;
    display: flex;
    flex-direction: column;
    align-items: center;
    justify-content: center;
    gap: 40px;
  }
  .card {
    position: relative;
    width: 680px;
    height: 388px;
    border-radius: 26px;
    overflow: hidden;
    box-shadow: 0 10px 28px var(--shadow);
  }

  /* Brand side with services */
  .card--logo-side {
    background: radial-gradient(ellipse at 45% 40%, var(--card-white) 40%, var(--card-mist) 100%);
    display: flex;
    flex-direction: column;
    align-items: center;
    padding: 38px 48px 0;
  }
  .card-art { position: absolute; inset: 0; width: 100%; height: 100%; }

  .brand { display: flex; flex-direction: column; align-items: flex-start; }
  .brand-row { display: flex; align-items: center; gap: 14px; }
  .brand-square { width: 34px; height: 34px; background: var(--brand-grey); }
  .brand-name {
    font-weight: 400;
    font-size: 40px;
    letter-spacing: 0.5px;
    color: var(--brand-blue);
    line-height: 1;
  }
  .brand-tagline {
    margin-top: 8px;
    margin-left: 48px;
    font-size: 17px;
    letter-spacing: 2px;
    color: var(--brand-grey);
  }
  .card--logo-side .brand-square { width: 28px; height: 28px; }
  .card--logo-side .brand-name { font-size: 32px; }
  .card--logo-side .brand-tagline { font-size: 14px; margin-left: 42px; margin-top: 6px; }

  .services {
    margin-top: 22px;
    width: 100%;
    color: var(--text-grey);
  }
  .services-title {
    font-weight: 600;
    font-size: 14px;
    letter-spacing: 1.5px;
    color: var(--brand-blue);
    margin-bottom: 8px;
  }
  .services-list { list-style: none; font-size: 11.5px; line-height: 1.6; letter-spacing: 0.3px; }
  .services-list li { display: flex; align-items: baseline; gap: 8px; }
  .services-list li::before {
    content: "";
    flex: none;
    width: 5px;
    height: 5px;
    background: var(--brand-blue);
    transform: translateY(-2px);
  }

  /* Contact side */
  .card--contact-side .brand {
    position: absolute;
    left: 190px;
    top: 60px;
  }
  .holder {
    position: absolute;
    left: 40px;
    top: 282px;
    color: var(--ink-light);
  }
  .holder-name { font-weight: 700; font-style: italic; font-size: 22px; line-height: 1.2; }
  .holder-title { font-style: italic; font-size: 19px; line-height: 1.2; }

  .contact-list {
    position: absolute;
    left: 450px;
    top: 226px;
    list-style: none;
    color: var(--ink-light);
    font-size: 13.5px;
    line-height: 1.25;
  }
  .contact-list li { display: flex; align-items: flex-start; gap: 7px; margin-bottom: 5px; }
  .contact-list li.address { margin-bottom: 8px; }
  .contact-icon { flex: none; width: 13px; height: 13px; margin-top: 2px; }
</style>
</head>
<body>

  <section class="card card--logo-side" aria-label="Business card, brand and services side">
    <div class="brand">
      <div class="brand-row">
        <span class="brand-square" aria-hidden="true"></span>
        <span class="brand-name">VANTOREQ Realty</span>
      </div>
      <span class="brand-tagline">REAL ESTATE SOLUTIONS</span>
    </div>
    <div class="services">
      <h2 class="services-title">REAL ESTATE INVESTMENTS</h2>
      <ul class="services-list">
        <li>BUY, RENOVATE, SELL AND RENT RESIDENTIAL PROPERTIES</li>
        <li>FULL HOME REHABBING, REMODELING AND INTERIOR DESIGN</li>
        <li>HOME STAGING SERVICES</li>
        <li>WHOLESALE INVESTOR PROPERTIES</li>
        <li>MAKE CASH OFFERS ON HOUSES IN ANY CONDITION AND IN ANY SITUATION</li>
        <li>PRIVATE MONEY INVESTOR PROGRAMS WITH 6-12% RETURNS</li>
        <li>PAY CASH REWARDS FOR REFERRALS</li>
        <li>CONCIERGE SERVICE</li>
      </ul>
    </div>
  </section>

  <section class="card card--contact-side" aria-label="Business card, contact side">
    <svg class="card-art" viewBox="0 0 680 388" preserveAspectRatio="none" aria-hidden="true">
      <defs>
        <radialGradient id="sheen" cx="0.45" cy="0.25" r="0.8">
          <stop offset="0.35" stop-color="#ffffff"/>
          <stop offset="1" stop-color="#dcdddf"/>
        </radialGradient>
      </defs>
      <rect width="680" height="388" fill="url(#sheen)"/>
      <path d="M0,196 C210,262 470,250 665,100" fill="none" stroke="var(--brand-blue)" stroke-width="12"/>
      <path d="M0,222 C210,285 470,272 680,92 L680,388 L0,388 Z" fill="var(--panel-grey)"/>
    </svg>

    <div class="brand">
      <div class="brand-row">
        <span class="brand-square" aria-hidden="true"></span>
        <span class="brand-name">VANTOREQ Realty</span>
      </div>
      <span class="brand-tagline">REAL ESTATE SOLUTIONS</span>
    </div>

    <div class="holder">
      <p class="holder-name">Daniel Hartwell</p>
      <p class="holder-title">Owner / C.E.O</p>
    </div>

    <ul class="contact-list">
      <li class="address">
        <svg class="contact-icon" viewBox="0 0 14 14" aria-hidden="true"><circle cx="7" cy="7" r="7" fill="#fff"/><path d="M3.5 7.5 L7 4 L10.5 7.5 M4.8 7 V10.5 H9.2 V7" fill="none" stroke="#909192" stroke-width="1.3"/></svg>
        <span>Suite # 418, Brook Plaza,<br>NY 10547</span>
      </li>
      <li>
        <svg class="contact-icon" viewBox="0 0 14 14" aria-hidden="true"><circle cx="7" cy="7" r="7" fill="#fff"/><path d="M4.5 3.5 L6 5.5 L5.2 6.6 Q6.2 8.4 7.6 9 L8.6 8.1 L10.5 9.6 L9.6 10.8 Q6 10.5 3.6 5 Z" fill="#909192"/></svg>
        <span>212-555-0148</span>
      </li>
      <li>
        <svg class="contact-icon" viewBox="0 0 14 14" aria-hidden="true"><circle cx="7" cy="7" r="7" fill="#fff"/><rect x="4.8" y="3" width="4.4" height="8" rx="0.8" fill="#909192"/></svg>
        <span>212-555-0193</span>
      </li>
      <li>
        <svg class="contact-icon" viewBox="0 0 14 14" aria-hidden="true"><circle cx="7" cy="7" r="7" fill="#fff"/><rect x="3.5" y="5.5" width="7" height="4.5" fill="#909192"/><rect x="5" y="3.5" width="4" height="2" fill="#909192"/></svg>
        <span>212-555-0176</span>
      </li>
      <li>
        <svg class="contact-icon" viewBox="0 0 14 14" aria-hidden="true"><circle cx="7" cy="7" r="7" fill="#fff"/><rect x="3.5" y="4.5" width="7" height="5" fill="#909192"/><path d="M3.5 4.5 L7 7.4 L10.5 4.5" fill="none" stroke="#fff" stroke-width="0.9"/></svg>
        <span>daniel@vantoreqrealty.com</span>
      </li>
      <li>
        <svg class="contact-icon" viewBox="0 0 14 14" aria-hidden="true"><circle cx="7" cy="7" r="7" fill="#fff"/><circle cx="7" cy="7" r="3.8" fill="none" stroke="#909192" stroke-width="1"/><path d="M3.2 7 H10.8 M7 3.2 V10.8" stroke="#909192" stroke-width="0.9"/></svg>
        <span>www.vantoreqrealty.com</span>
      </li>
    </ul>
  </section>

</body>
</html>
```